New Flyer Design Project - for sale units at The Lodge phase 3

on attached the A2 is full kitchen 1 bedroom, the A3 is gally kitchen and the B2 is the the 2 bedroom, on attached pictures the room with 2 queen beds is only for the 2 bedroom

This is going to be used to sale the units (real estate sale) so the layout could possibly be text and then pictures maybe 1 bedroom on one side and 2 on the back?

Experience the Modern Luxury of the New Phase 3 Building of the
Lodge at Harrow Bend

* Opening Spring 2019

* America's #17 Family Resort; Tennessee's Only Ranked Resort

1 Bedroom Bunk Suite (Galley Kitchen) - $199,000; Sleeps 6

* Private King Master Bedroom

* Bunk Bed Galley

* Granite Counters Throughout

* Fully Furnished with Custom Furnishings

* Private Balcony

* Equipped Galley Kitchen

* In Unit Laundry

* Queen Sleeper Sofa

1 Bedroom Bunk Suite (Full Kitchen) - $209,000; Sleeps 6

* Bunk Bed Galley

* Granite Counters throughout

* Equipped Full Kitchen

* Completely Furnished with Custom Furnishings

* Private Balcony

* In Unit Laundry

* Queen Sleeper Sofa

2 Bedroom Bunk Suite (Full Kitchen) - $249,000; Sleeps 10

* Private King Master Bedroom with On-Suite Bathroom

* Two Queen Bedroom

* Bunk Bed Galley

* Full Kitchen

* Private Balcony

* In Unit Laundry

* Queen Sleeper Sofa

Target Market(s)

people wanting to buy units in phase 3 of The Lodge at Harrow Bend

Industry/Entity Type

Real Estate Development

Requirements
Must have
• attached text to describe units and price
• pictures and layouts
• Contact Dale Porter
• 865-391-7702 Dale@bramblecrestlodges.example
Nice to have
• brand and logo
Should not have
• it should not be plain this is m ore of a luxury project

```html
<!DOCTYPE html>
<html lang="en">
<head>
<meta charset="utf-8">
<title>The Lodge at Harrow Bend – Phase 3 Sales Flyers</title>
<link rel="stylesheet" href="https://fonts.googleapis.com/css2?family=Lato:wght@400;700;900&display=swap">
<style>
  :root {
    --backdrop: #8c8a8b;
    --paper: #fbfafa;
    --teal: #4f7b80;
    --teal-deep: #426b70;
    --gold: #d59f5c;
    --ink: #1f1f1f;
    --on-teal: #ffffff;
    --black: #0d0d0d;
    --plan-wall: #4e4036;
    --plan-floor: #d8cfbd;
    --plan-tile: #c4b9a3;
    --plan-blue: #2f6aa0;
    --photo-light: #e7e4d8;
    --photo-green: #97a476;
    --photo-dark: #3e3a34;
  }
  * { box-sizing: border-box; margin: 0; padding: 0; }
  html, body {
    width: 1200px; height: 1200px; overflow: hidden;
    background: var(--backdrop);
    font-family: 'Lato', sans-serif;
    color: var(--ink);
  }
  .canvas { position: relative; width: 1200px; height: 1200px; }
  .flyer {
    position: absolute; left: 406px;
    width: 407px; height: 570px;
    background: var(--paper);
    transform: scale(0.8); transform-origin: top left;
    overflow: hidden;
    box-shadow: 3px 4px 6px rgba(0,0,0,0.35);
  }
  .flyer--two-bedroom { top: 102px; }
  .flyer--one-bedroom { top: 638px; }
  .flyer > * { position: absolute; }

  .floor-plan {
    background:
      radial-gradient(ellipse at 65% 30%, rgba(47,106,160,0.28) 0%, rgba(47,106,160,0) 38%),
      radial-gradient(ellipse at 45% 60%, rgba(181,110,58,0.22) 0%, rgba(181,110,58,0) 35%),
      linear-gradient(160deg, var(--plan-floor) 0%, var(--plan-tile) 100%);
    border: 6px solid var(--plan-wall);
  }
  .room-photo {
    background:
      linear-gradient(180deg, rgba(62,58,52,0.55) 0%, rgba(62,58,52,0) 30%),
      linear-gradient(100deg, var(--photo-green) 0%, #c9ceb0 30%, var(--photo-light) 55%, #f4f2ec 75%, #b9b4a5 100%);
  }
  .kitchen-photo {
    background:
      linear-gradient(180deg, rgba(60,55,50,0.35) 0%, rgba(60,55,50,0) 40%),
      linear-gradient(105deg, #8e9ea6 0%, #d9dbd6 45%, #f0efea 60%, #2f2b28 100%);
  }
  .plan-thumb {
    background:
      radial-gradient(ellipse at 70% 35%, rgba(47,106,160,0.35) 0%, rgba(47,106,160,0) 40%),
      linear-gradient(135deg, #4a1d1a 0%, var(--plan-floor) 22%, var(--plan-tile) 80%, #4a1d1a 100%);
  }

  .brand {
    display: flex; align-items: center; justify-content: center;
    text-align: center;
    font-weight: 900; font-size: 18px; line-height: 1.2;
    color: var(--teal);
  }

  .headline {
    background: var(--teal); color: var(--on-teal);
    font-size: 16.5px; line-height: 21px; font-weight: 700;
    padding: 10px 6px 0 12px;
  }
  .opening {
    background: var(--gold); color: #fff;
    font-size: 22px; line-height: 27px; font-weight: 700; text-align: right;
    padding: 0 13px 0 0;
  }
  .opening--band { font-size: 24px; line-height: 44px; padding-right: 13px; }

  .ranking {
    font-size: 12.5px; line-height: 21px; font-weight: 700; padding-left: 12px;
    white-space: nowrap;
  }
  .ranking--gold { background: var(--gold); color: var(--ink); }
  .ranking--teal { background: var(--teal); color: var(--on-teal); }

  .suite-title { left: 12px; font-size: 14px; font-weight: 700; white-space: nowrap; }
  .suite-title .price { color: var(--gold); font-size: 19px; font-weight: 700; }
  .sleeps { left: 12px; font-size: 14px; font-weight: 700; }

  .features { list-style: none; font-size: 6px; line-height: 13.6px; }
  .features li { position: relative; padding-left: 12px; white-space: nowrap; }
  .features li::before {
    content: ""; position: absolute; left: 1px; top: 6px;
    width: 3px; height: 3px; border-radius: 50%; background: var(--gold);
  }

  .contact {
    left: 0; width: 407px; height: 35px; top: 522px;
    background: var(--gold);
    text-align: center; font-size: 6px; line-height: 8.6px; font-weight: 700;
    padding-top: 5px; color: var(--ink);
  }
  .base-bar { left: 0; width: 407px; top: 557px; height: 13px; background: var(--black); }
</style>
</head>
<body>
<div class="canvas">

  <section class="flyer flyer--two-bedroom">
    <div class="floor-plan" style="left:0;top:0;width:222px;height:260px" role="img" aria-label="Floor plan of the 2 bedroom bunk suite"></div>
    <div class="brand" style="left:222px;top:0;width:185px;height:119px">The Lodge<br>at Harrow Bend</div>
    <div class="room-photo" style="left:230px;top:119px;width:177px;height:141px" role="img" aria-label="Photo of the bedroom with two queen beds"></div>

    <div class="headline" style="left:0;top:268px;width:275px;height:84px">Experience the Modern Luxury of the New Phase 3 Building of the Lodge at Harrow Bend</div>
    <div class="opening" style="left:282px;top:268px;width:125px;height:84px">Opening<br>Spring<br>2019</div>

    <div class="ranking ranking--gold" style="left:0;top:359px;width:192px;height:21px">America's #17 Family Resort</div>
    <div class="ranking ranking--teal" style="left:196px;top:359px;width:211px;height:21px">Tennessee's Only Ranked Resort</div>

    <h2 class="suite-title" style="top:387px">2 Bedroom Bunk Suite (Full Kitchen) - <span class="price">$249,000</span></h2>
    <p class="sleeps" style="top:416px">Sleeps 10</p>

    <ul class="features" style="left:12px;top:443px;width:260px">
      <li>Private King Master Bedroom with On-Suite Bathroom</li>
      <li>Bunk Bed Galley</li>
      <li>Granite Counters Throughout</li>
      <li>Two Queen Bedroom</li>
      <li>Completely Furnished with Custom Furnishings</li>
    </ul>
    <ul class="features" style="left:279px;top:443px;width:120px">
      <li>Full Kitchen</li>
      <li>Private Balcony</li>
      <li>In Unit Laundry</li>
      <li>Queen Sleeper Sofa</li>
    </ul>

    <div class="contact">Dale Porter<br>865-391-7702<br>Dale@bramblecrestlodges.example</div>
    <div class="base-bar"></div>
  </section>

  <section class="flyer flyer--one-bedroom">
    <div class="floor-plan" style="left:0;top:0;width:212px;height:178px" role="img" aria-label="Floor plan of the 1 bedroom bunk suite"></div>
    <div class="brand" style="left:212px;top:0;width:195px;height:138px">The Lodge<br>at Harrow Bend</div>

    <div class="opening opening--band" style="left:153px;top:138px;width:254px;height:44px">Opening Spring 2019</div>

    <div class="headline" style="left:0;top:182px;width:275px;height:86px">Experience the Modern Luxury of the New Phase 3 Building of the Lodge at Harrow Bend</div>
    <div class="room-photo" style="left:275px;top:182px;width:132px;height:86px" role="img" aria-label="Photo of the king master bedroom"></div>

    <div class="ranking ranking--gold" style="left:0;top:268px;width:192px;height:20px">America's #17 Family Resort</div>
    <div class="ranking ranking--teal" style="left:192px;top:268px;width:215px;height:20px">Tennessee's Only Ranked Resort</div>

    <h2 class="suite-title" style="top:304px">1 Bedroom Bunk Suite (Galley Kitchen) - <span class="price">$199,000</span></h2>
    <p class="sleeps" style="top:326px">Sleeps 6</p>
    <ul class="features" style="left:12px;top:344px;width:200px">
      <li>Private King Master Bedroom</li>
      <li>Bunk Bed Galley</li>
      <li>Granite Counters Throughout</li>
      <li>Fully Furnished with Custom Furnishings</li>
    </ul>
    <ul class="features" style="left:210px;top:344px;width:100px">
      <li>Equipped Galley Kitchen</li>
      <li>Private Balcony</li>
      <li>In Unit Laundry</li>
      <li>Queen Sleeper Sofa</li>
    </ul>
    <div class="kitchen-photo" style="left:312px;top:334px;width:93px;height:71px" role="img" aria-label="Photo of the galley kitchen and dining area"></div>

    <h2 class="suite-title" style="top:413px">1 Bedroom Bunk Suite (Full Kitchen) - <span class="price">$209,000</span></h2>
    <p class="sleeps" style="top:435px">Sleeps 6</p>
    <ul class="features" style="left:12px;top:453px;width:200px">
      <li>Private King Master Bedroom</li>
      <li>Bunk Bed Galley</li>
      <li>Granite Counters Throughout</li>
      <li>Completely Furnished with Custom Furnishings</li>
    </ul>
    <ul class="features" style="left:210px;top:453px;width:100px">
      <li>Equipped Galley Kitchen</li>
      <li>Private Balcony</li>
      <li>In Unit Laundry</li>
      <li>Queen Sleeper Sofa</li>
    </ul>
    <div class="plan-thumb" style="left:311px;top:436px;width:96px;height:86px" role="img" aria-label="Floor plan of the 1 bedroom full kitchen suite"></div>

    <div class="contact">Dale Porter<br>865-391-7702<br>Dale@bramblecrestlodges.example</div>
    <div class="base-bar"></div>
  </section>

</div>
</body>
</html>
```